New Business Card Design Project

We are looking for a talented individual to create a truly awesome/unique business card design for us. We are looking for a someone to design something that will really stand out from the crowd - we don't mind what ideas you come up with (ie embossed/flat/matte/shine etc etc) just wow us with your creativity.
Updates

Sick

Target Market(s)

Video Games Industry Professionals (all levels of seniority from QA Testers through to CEOs)

Contact Information for Business Card

Company logo (see upload)
Company name: Northbridge Play Careers Ltd
Employee Name: Harriet Vasko
Job title: CEO
Website: www.npc2go.com
Office +44 1632 960418
Mobile: +44 7700 900582
Email: harriet@npc2go.com

Colors

Designer to choose colors to be used in the design.

Requirements
Must have
• The business card design MUST contain all the information listed in the BUSINESS CARD DETAILS box.
• You will see the colours that are relevant to us (ie company logo) in the uploaded imagery - however you do not have to use all these colours when designing the business card itself
• MUST BE DOUBLE SIDED

```html
<!DOCTYPE html>
<html lang="en">
<head>
<meta charset="utf-8">
<title>Northbridge Play Careers – Business Card</title>
<link rel="stylesheet" href="https://fonts.googleapis.com/css2?family=Open+Sans:wght@400&family=Ubuntu:wght@400;700&display=swap">
<style>
  :root {
    --backdrop: #5b5b5b;
    --card-light: #f3f3f3;
    --navy: #1c2d5e;
    --orange: #f47b20;
    --ink: #333333;
    --white: #ffffff;
  }
  * { margin: 0; padding: 0; box-sizing: border-box; }
  html, body {
    width: 1200px; height: 900px; overflow: hidden;
    background: var(--backdrop);
  }
  .stage { position: relative; width: 1200px; height: 900px; }

  .card {
    position: absolute; top: 200px; width: 310px; height: 502px;
  }
  .card-front {
    left: 253px; background: var(--card-light);
    border-radius: 62px 0 62px 0;
  }
  .card-back {
    left: 627px; background: var(--navy);
    border-radius: 0 62px 0 62px;
    display: flex; align-items: center; justify-content: center;
  }

  .brand {
    position: absolute; left: 0; right: 0; top: 80px;
    display: flex; flex-direction: column; align-items: center; gap: 22px;
  }
  .brand-dot {
    width: 74px; height: 74px; border-radius: 50%; background: var(--navy);
  }
  .brand-name {
    font-family: "Ubuntu", sans-serif; font-weight: 700;
    font-size: 27px; line-height: 32px; text-align: center;
    color: var(--navy);
  }
  .card-back .brand-name { color: var(--white); font-size: 29px; line-height: 35px; }

  .holder { position: absolute; left: 33px; top: 341px; }
  .holder-name {
    font-family: "Ubuntu", sans-serif; font-weight: 400;
    font-size: 20px; line-height: 24px; color: var(--navy);
  }
  .holder-title {
    font-family: "Open Sans", sans-serif; font-size: 13px; line-height: 18px;
    color: var(--orange);
  }
  .contacts { list-style: none; margin-top: 8px; }
  .contacts li {
    display: flex; align-items: center; gap: 5px;
    font-family: "Open Sans", sans-serif; font-size: 14px; line-height: 18.5px;
    color: var(--ink);
  }
  .contacts svg { width: 11px; height: 11px; fill: var(--navy); flex: none; }
</style>
</head>
<body>
<div class="stage">

  <section class="card card-front">
    <div class="brand">
      <span class="brand-dot"></span>
      <p class="brand-name">Northbridge<br>Play Careers</p>
    </div>

    <div class="holder">
      <p class="holder-name">Harriet Vasko</p>
      <p class="holder-title">CEO</p>
      <ul class="contacts">
        <li>
          <svg viewBox="0 0 12 12" aria-hidden="true"><path d="M1 4.5C1 3 3 2 6 2s5 1 5 2.5v1H8.5V4.3C7.8 4 4.2 4 3.5 4.3v1.2H1z"/><rect x="2.5" y="6" width="7" height="4.5" rx="1"/></svg>
          +44 1632 960418
        </li>
        <li>
          <svg viewBox="0 0 12 12" aria-hidden="true"><path d="M3.5 0.5h5a1 1 0 0 1 1 1v9a1 1 0 0 1-1 1h-5a1 1 0 0 1-1-1v-9a1 1 0 0 1 1-1zM4 2v7h4V2z"/></svg>
          +44 7700 900582
        </li>
        <li>
          <svg viewBox="0 0 12 12" aria-hidden="true"><path d="M1 2.5h10v7H1z M1.6 3.2L6 6.6l4.4-3.4v-0.3H1.6z" fill-rule="evenodd"/></svg>
          harriet@npc2go.com
        </li>
        <li>
          <svg viewBox="0 0 12 12" aria-hidden="true"><circle cx="6" cy="6" r="5"/></svg>
          www.npc2go.com
        </li>
      </ul>
    </div>
  </section>

  <section class="card card-back">
    <p class="brand-name">Northbridge<br>Play Careers</p>
  </section>

</div>
</body>
</html>
```